Fantasy Sports Website re-Design

We need a website designed for our fantasy sports website. The website is TorvexPlay.com . An example of the website layout would be like : https://www.quandrel.com/fantasy-sports/fantasy-sports-solutions. We like this site, because of the screenshots on 1 side and a description on the other side. This layout style will showcase the features we have on our site. Somewhere in the header there will be a video explaining what the site is. We would like the style to be black and gold. Like a casino. Attached is an example logo to give the style we want.

Target Market(s)

fantasy sports

Number of Pages Required

3 page

Colors
fecb35
000000

Requirements
Must have
• mockups of index page
Nice to have
• mockups of sub pages

```html
<!DOCTYPE html>
<html lang="en">
<head>
<meta charset="utf-8">
<title>TorvexPlay – Fantasy Sports</title>
<link href="https://fonts.googleapis.com/css2?family=Open+Sans:wght@400;600;700;800&display=swap" rel="stylesheet">
<style>
:root{
  --gold:#fecb35;
  --black:#000000;
  --ink:#1a1a1a;
  --white:#ffffff;
  --grey:#efefef;
  --line:#d9d9d9;
  --blue:#2d6db5;
  --number:#a8893a;
  --muted:#6b6b6b;
}
*{box-sizing:border-box;margin:0;padding:0}
html,body{width:1200px;height:3704px;overflow:hidden}
body{font-family:'Open Sans',Arial,sans-serif;color:var(--ink);background:var(--white);position:relative}
section,header,footer{position:absolute;left:0;width:1200px;overflow:hidden}
.abs{position:absolute}

/* header */
.topbar{top:0;height:12px;background:var(--black)}
.site-header{top:12px;height:136px;background:var(--white)}
.brand{left:99px;top:28px;display:flex;align-items:center;gap:10px;font-weight:800;font-size:34px;color:var(--black);letter-spacing:-.5px}
.brand-dot{width:22px;height:22px;border-radius:50%;background:var(--gold)}
.contact-line{right:99px;font-size:15px;display:flex;align-items:center;gap:8px}
.nav{left:99px;top:92px;width:1002px;height:44px;background:var(--gold);display:flex;align-items:center}
.nav a{font-size:16px;color:var(--black);text-decoration:none;padding:0 15.5px;height:44px;line-height:44px}
.nav a.active{background:var(--black);color:var(--white);padding:0 10px}

/* hero */
.hero{top:148px;height:457px;background:radial-gradient(ellipse at 40% 20%,#3f6fb3 0%,#173a78 35%,#0b1a3a 70%,#05080f 100%)}

/* about */
.about{top:605px;height:413px;background:var(--gold)}
.section-title{font-weight:600;font-size:30px;color:var(--black)}
.about .section-title{left:99px;top:52px}
.underline{height:3px;background:var(--black)}
.about .underline{left:99px;top:98px;width:140px}
.about p{left:99px;top:150px;width:590px;font-size:21px;line-height:39px;color:var(--black)}
.about-figure{left:790px;top:20px;width:250px;height:375px;background:linear-gradient(180deg,#f2f2f2 0%,#dcdcdc 60%,#3a3a3a 100%);border-radius:40px 40px 10px 10px}

/* services */
.services{top:1018px;height:600px;background:var(--white)}
.center-title{width:1200px;text-align:center;font-size:30px;font-weight:600;color:var(--black)}
.services .center-title{top:62px}
.gold-rule{left:520px;width:160px;height:3px;background:var(--gold)}
.services .gold-rule{top:112px}
.diagram{left:0;top:0}
.svc-label{font-size:15px;font-weight:600;color:var(--black);line-height:19px}
.hub{left:0;width:1200px;top:370px;text-align:center;font-size:36px;font-weight:600;line-height:50px;color:var(--black)}

/* why */
.why{top:1618px;height:523px;background:var(--gold)}
.why h2{left:99px;top:24px;font-size:26px;font-weight:700;color:var(--black)}
.why-item{left:99px;width:500px;display:flex;gap:20px}
.why-num{width:66px;font-size:66px;font-weight:700;color:var(--number);line-height:60px}
.why-item h3{font-size:17px;font-weight:700;color:var(--black);margin-top:-4px;margin-bottom:4px}
.why-item p{font-size:13px;line-height:17px;color:var(--ink);width:410px}
.video{left:627px;top:123px;width:474px;height:267px;background:linear-gradient(135deg,#2a3a55 0%,#55607a 45%,#1b1f2a 100%)}
.video-bar{left:0;bottom:0;width:474px;height:24px;background:#111}
.play{left:207px;top:105px;width:60px;height:44px}

/* motivation */
.motivation{top:2141px;height:526px;background:linear-gradient(100deg,#1a2430 0%,#2e3a46 40%,#3a2824 70%,#141414 100%)}
.quote{left:101px;top:160px;width:640px;font-size:22px;line-height:39px;color:var(--white)}
.btn-gold{background:var(--gold);color:var(--black);font-size:15px;font-weight:600;display:inline-block}
.read-more{left:101px;top:356px;padding:5px 10px}
.lobby{left:773px;top:91px;width:328px;height:275px;background:var(--white);box-shadow:0 4px 14px rgba(0,0,0,.4);font-size:11px;color:var(--ink)}
.lobby-tabs{display:flex;gap:28px;padding:14px 20px 0;font-weight:700;font-size:12px;height:44px;border-bottom:1px solid var(--line)}
.lobby-tabs .on{color:var(--blue);border-bottom:2px solid var(--blue);height:30px}
.lobby-sub{display:flex;gap:22px;padding:12px 20px 0;font-size:11px;color:var(--muted);height:38px}
.lobby-sub .on{color:var(--blue);border-bottom:2px solid var(--blue);height:18px}
.lobby-head{padding:8px 20px;font-weight:700;font-size:11px}
.lobby-row{display:grid;grid-template-columns:110px 50px 60px 60px;padding:4px 20px;align-items:center;font-size:10px}
.lobby-row.head{color:var(--muted);border-bottom:1px solid var(--line)}
.lobby-row .win{color:#1aa34a;font-weight:700}
.avatar-dot{display:inline-block;width:26px;height:26px;border-radius:50%;color:var(--white);font-size:10px;font-weight:700;text-align:center;line-height:26px;margin-right:6px;vertical-align:middle}
.more-btn{left:1005px;top:392px;padding:6px 24px;font-size:17px}

/* testimonials */
.testimonials{top:2667px;height:502px;background:var(--grey)}
.testimonials .center-title{top:56px}
.testimonials .gold-rule{top:106px;left:530px;width:140px}
.client-photo{left:533px;top:148px;width:134px;height:134px;border-radius:50%;border:3px solid var(--gold);background:radial-gradient(circle at 50% 70%,#d92a2a 0%,#f3f3f3 70%)}
.testimonial-text{left:230px;top:316px;width:740px;text-align:center;font-size:15px;line-height:22px;color:var(--ink)}
.dots{left:579px;top:437px;display:flex;gap:6px}
.dots span{width:10px;height:10px;border-radius:50%;background:var(--black)}
.dots span.on{background:var(--gold)}

/* contact */
.contact{top:3169px;height:481px;background:#101010;color:var(--white)}
.contact-tag{left:99px;top:0;width:212px;height:62px;background:var(--gold);color:var(--black);font-size:28px;font-weight:600;line-height:62px;padding-left:12px;clip-path:polygon(0 0,84% 0,100% 100%,0 100%)}
.info{left:99px;display:flex;gap:14px;font-size:13px;line-height:17px}
.icon-circle{width:24px;height:24px;border-radius:50%;background:var(--gold);flex:none;display:flex;align-items:center;justify-content:center}
.info strong{font-size:15px;font-weight:700;display:block;margin-bottom:2px}
.links{left:440px;top:128px}
.links h4{font-size:16px;font-weight:600;margin-bottom:14px}
.links li{list-style:none;font-size:12px;height:31px;padding-left:24px;position:relative}
.links li::before{content:"";position:absolute;left:0;top:6px;width:5px;height:5px;border-radius:50%;background:var(--white)}
.form{left:704px;top:79px;width:397px;height:331px;background:#e9e9e9;padding:22px 16px;color:var(--ink)}
.form h4{font-size:20px;font-weight:600;margin-bottom:14px}
.field{background:var(--white);height:44px;margin-bottom:11px;padding:10px 8px;font-size:13px;color:var(--muted)}
.field.tall{height:84px}
.submit{position:absolute;right:16px;bottom:18px;padding:6px 20px;font-size:13px}

.site-footer{top:3650px;height:54px;background:var(--gold);font-size:12px;color:var(--black);padding:24px 99px}
</style>
</head>
<body>

<header class="topbar"></header>
<header class="site-header">
  <div class="abs brand"><span class="brand-dot"></span>TorvexPlay</div>
  <div class="abs contact-line" style="top:20px">
    <svg width="16" height="16" viewBox="0 0 24 24"><path d="M6.6 10.8a15 15 0 0 0 6.6 6.6l2.2-2.2c.3-.3.7-.4 1-.2 1.1.4 2.3.6 3.6.6.6 0 1 .4 1 1V20c0 .6-.4 1-1 1A17 17 0 0 1 3 4c0-.6.4-1 1-1h3.5c.6 0 1 .4 1 1 0 1.2.2 2.4.6 3.6.1.3 0 .7-.2 1z" fill="#000"/></svg>
    01632 960418
  </div>
  <div class="abs contact-line" style="top:48px">
    <svg width="20" height="14" viewBox="0 0 20 14"><rect x="1" y="1" width="18" height="12" fill="none" stroke="#000" stroke-width="1.5"/><path d="M1 1l9 7 9-7" fill="none" stroke="#000" stroke-width="1.5"/></svg>
    sales@torvexplay.example
  </div>
  <nav class="abs nav">
    <a class="active">Home</a><a>About</a><a>Work Blog</a><a>Career</a><a>Contact</a><a>Social Network</a><a>Healthcare</a><a>Digital</a><a>Fantsy Sports</a>
  </nav>
</header>

<section class="hero" role="img" aria-label="Stadium at night with floodlights and athletes from basketball, football, rugby and cricket leaping into the air"></section>

<section class="about">
  <h2 class="abs section-title">About Us</h2>
  <div class="abs underline"></div>
  <p class="abs">A team who has a history of successfully delivering custom &amp; white label daily or season long fantasy sports website &amp; mobile application. A team that can help you understand, execute and successfully setup a revenue driven fantasy sports business.</p>
  <div class="abs about-figure" role="img" aria-label="Footballer in a white kit kicking a ball"></div>
</section>

<section class="services">
  <h2 class="abs center-title">Our Services</h2>
  <div class="abs gold-rule"></div>
  <svg class="abs diagram" width="1200" height="600" viewBox="0 0 1200 600">
    <path d="M300 470 C 320 120, 880 120, 900 470" fill="none" stroke="#dcdcdc" stroke-width="12"/>
    <!-- leader lines -->
    <polyline points="120,218 260,218 318,260" fill="none" stroke="#2d6db5" stroke-width="2"/>
    <polyline points="95,398 215,398 240,420" fill="none" stroke="#2d6db5" stroke-width="2"/>
    <polyline points="1080,218 940,218 880,262" fill="none" stroke="#2d6db5" stroke-width="2"/>
    <polyline points="1105,398 985,398 955,420" fill="none" stroke="#2d6db5" stroke-width="2"/>
    <g fill="#ffffff" stroke="#e3e3e3" stroke-width="6">
      <circle cx="336" cy="303" r="58"/><circle cx="264" cy="464" r="58"/>
      <circle cx="855" cy="316" r="58"/><circle cx="924" cy="464" r="58"/>
    </g>
    <g fill="none" stroke="#2d6db5" stroke-width="6">
      <path d="M280 340 A66 66 0 0 1 300 248"/>
      <path d="M210 505 A66 66 0 0 1 228 408"/>
      <path d="M910 280 A66 66 0 0 1 892 370"/>
      <path d="M978 420 A66 66 0 0 1 960 520"/>
    </g>
    <circle cx="336" cy="303" r="40" fill="#8a3a2a"><title>Casino and betting items</title></circle>
    <circle cx="264" cy="464" r="40" fill="#c46a2a"><title>Assorted sports balls</title></circle>
    <circle cx="855" cy="316" r="40" fill="#5a8ac8"><title>Media and business icons</title></circle>
    <circle cx="924" cy="464" r="40" fill="#e9eef5"><title>League emblem</title></circle>
  </svg>
  <div class="abs svc-label" style="left:125px;top:180px">Sports Betting and<br>Casino Operators</div>
  <div class="abs svc-label" style="left:97px;top:375px">Sports Startup</div>
  <div class="abs svc-label" style="right:120px;top:180px;text-align:right">Media and other<br>Business</div>
  <div class="abs svc-label" style="right:97px;top:375px">Sports Leagues</div>
  <div class="abs hub">TorvexPlay Sports<br>Specialists</div>
</section>

<section class="why">
  <h2 class="abs">Why TorvexPlay sports website design?</h2>
  <div class="abs why-item" style="top:92px"><div class="why-num">1.</div><div><h3>Pre to post launch partners</h3><p>We are your partners right from the day you start planning your business to the time you achieve desired success.</p></div></div>
  <div class="abs why-item" style="top:186px"><div class="why-num">2.</div><div><h3>Multiple sports support</h3><p>Name the sports or event and you have it in your platform. With 7 years of experience.</p></div></div>
  <div class="abs why-item" style="top:282px"><div class="why-num">3.</div><div><h3>End-user empathy</h3><p>Not only do we understand your vision, but also the needs of sports fans. We do a complete analysis of the targeted end-users and ensure instant emotional connection with the end-users.</p></div></div>
  <div class="abs why-item" style="top:400px"><div class="why-num">4.</div><div><h3>Seal of approval</h3><p>As a proud member of FPLA (Fantasy Play League Alliance), we work closely with people who matter within the industry. We love to learn, network and grow with the fantasy sports industry.</p></div></div>
  <div class="abs video" role="img" aria-label="Video explaining the site, still of two footballers celebrating">
    <svg class="abs play" viewBox="0 0 60 44"><circle cx="30" cy="22" r="21" fill="rgba(0,0,0,.55)"/><path d="M24 13l16 9-16 9z" fill="#fff"/></svg>
    <div class="abs video-bar"></div>
  </div>
</section>

<section class="motivation" role="img" aria-label="Sprinter in starting position on a running track at dusk">
  <p class="abs quote">We can't live in an island that is encircled by poverty.<br>We all breathe the same air.<br>We must give a chance to everyone, at least a basic chance.</p>
  <span class="abs btn-gold read-more">Read More</span>
  <div class="abs lobby">
    <div class="lobby-tabs"><span class="on">Lobby</span><span>My Contests</span><span>News</span><span>Leaderboard</span></div>
    <div class="lobby-sub"><span>LIVE</span><span>UPCOMING</span><span class="on">COMPLETED</span></div>
    <div class="lobby-head">Weekend Special</div>
    <div class="lobby-row head"><span>League</span><span>Team</span><span>Rank</span><span>Won</span></div>
    <div class="lobby-row"><span><i class="avatar-dot" style="background:#2d8ad1">KP</i>King of the pitch</span><span>Team-1</span><span>6/400</span><span class="win">$ 1,000</span></div>
    <div class="lobby-row"><span><i class="avatar-dot" style="background:#f0a030">S</i>Striker</span><span>Team-2</span><span>320/400</span><span class="win">$ 800</span></div>
  </div>
  <span class="abs btn-gold more-btn">More</span>
</section>

<section class="testimonials">
  <h2 class="abs center-title">Our Testimonials</h2>
  <div class="abs gold-rule"></div>
  <div class="abs client-photo" role="img" aria-label="Client portrait in a red sports shirt"></div>
  <p class="abs testimonial-text">On this page you can explore the sports taking place, see featured schools using Rallyboard sport, read latest news, respond to fixture requests posted by schools and find out more about Rallyboard sport, the various add-on modules and how to get started</p>
  <div class="abs dots"><span></span><span class="on"></span><span></span></div>
</section>

<section class="contact">
  <div class="abs contact-tag">Contact Us</div>
  <div class="abs info" style="top:140px">
    <span class="icon-circle"><svg width="12" height="14" viewBox="0 0 12 16"><path d="M6 0a6 6 0 0 0-6 6c0 4.5 6 10 6 10s6-5.5 6-10a6 6 0 0 0-6-6zm0 8.5A2.5 2.5 0 1 1 6 3.5a2.5 2.5 0 0 1 0 5z" fill="#000"/></svg></span>
    <div><strong>Head Office</strong>420 Brindle Ave<br>Suite 12<br>Westmoor, NJ 07999</div>
  </div>
  <div class="abs info" style="top:250px;align-items:center">
    <span class="icon-circle"><svg width="12" height="12" viewBox="0 0 24 24"><path d="M6.6 10.8a15 15 0 0 0 6.6 6.6l2.2-2.2c.3-.3.7-.4 1-.2 1.1.4 2.3.6 3.6.6.6 0 1 .4 1 1V20c0 .6-.4 1-1 1A17 17 0 0 1 3 4c0-.6.4-1 1-1h3.5c.6 0 1 .4 1 1 0 1.2.2 2.4.6 3.6.1.3 0 .7-.2 1z" fill="#000"/></svg></span>
    <span style="font-size:14px">+3650001234</span>
  </div>
  <div class="abs info" style="top:312px;align-items:center">
    <span class="icon-circle"><svg width="12" height="9" viewBox="0 0 20 14"><rect x="1" y="1" width="18" height="12" fill="none" stroke="#000" stroke-width="2"/><path d="M1 1l9 7 9-7" fill="none" stroke="#000" stroke-width="2"/></svg></span>
    <span style="font-size:14px">hello@torvexplay.example</span>
  </div>
  <div class="abs links">
    <h4>Quick Links</h4>
    <ul><li>HOME</li><li>ABOUT US</li><li>OUR PRODUCTS</li><li>OCEAN STORE</li><li>PORTABLE OCEAN</li><li>TRACEABILITY</li><li>CONTACT US</li></ul>
  </div>
  <div class="abs form">
    <h4>Contact form</h4>
    <div class="field">Name</div>
    <div class="field">Email</div>
    <div class="field tall">Message</div>
    <span class="btn-gold submit">SUBMIT</span>
  </div>
</section>

<footer class="site-footer">TorvexPlay© 2018 Privacy Policy</footer>

</body>
</html>
```